Verimonta PowerPoint Sales Deck

I need a Professional, eye-popping Verimonta Sales Slide deck that I can present to potential new customers via web conference. Verimonta is the first company to invent a digital sign-in kiosk that prints a name badge for visitors that is specifically designed for Nursing Homes and Assisted Living facilities. When a visitor sign's in the kiosk will screen the person for a criminal background, TB and to make sure they have proper insurance requirements. At the end of the day, the Verimonta sign-in kiosk adds a layer of protection to the community. I need the finished product in a PowerPoint Format

Target Market(s)

Assisted Living and Nursing Homes Owners and Operators

Requirements
Must have
• Must look professional, innovative and clean. Must have Logo.
• Color #
• Green: #3fa863
• Blue: #384275
• Need a well-designed and creative way to play a video on the 5 slides. I couldnt get it to look right?

```html
<!DOCTYPE html>
<html lang="en">
<head>
<meta charset="utf-8">
<title>Verimonta Sales Deck – Slide Overview</title>
<link href="https://fonts.googleapis.com/css2?family=Open+Sans:wght@400;600;700&display=swap" rel="stylesheet">
<style>
:root{
  --green:#3fa863;
  --blue:#384275;
  --grey:#6f6f6f;
  --text:#8a8a8a;
  --light:#f4f6f8;
  --white:#ffffff;
  --map:#e9ebee;
}
*{box-sizing:border-box;margin:0;padding:0}
html,body{width:1200px;height:1109px;overflow:hidden;background:var(--white)}
body{font-family:"Open Sans",Arial,sans-serif;position:relative;color:var(--text)}
.slide{position:absolute;width:383px;height:215px;background:var(--white);overflow:hidden;box-shadow:0 0 3px rgba(0,0,0,.18)}
.c1{left:8px}.c2{left:408px}.c3{left:807px}
.r1{top:0}.r2{top:222px}.r3{top:444px}.r4{top:666px}.r5{top:888px}
.abs{position:absolute}
.title{position:absolute;left:17px;top:15px;font-size:15.5px;color:var(--blue);white-space:nowrap}
.title .g{color:var(--green)}
.title .u{border-bottom:1.5px solid var(--green);padding-bottom:1px}
.logo{position:absolute;right:14px;top:10px;display:flex;align-items:center;gap:3px;font-size:8.5px;font-weight:600;color:var(--blue)}
.logo i{width:7px;height:7px;border-radius:50%;background:var(--green);display:block}
.logo.w{color:var(--white)}
.logo.w i{background:var(--white)}
.logo.lg{font-size:13px}
.logo.lg i{width:10px;height:10px}
.footer{position:absolute;left:0;right:0;bottom:0;height:8px;background:var(--blue);font-size:3.6px;color:#d8dbe8;padding-left:5px;line-height:8px}
.footer .num{position:absolute;right:13px;top:0;width:13px;height:8px;background:var(--white);color:var(--grey);text-align:center}
.footer .end{position:absolute;right:0;top:0;width:13px;height:8px;background:var(--green)}
.lead{font-size:8px;color:#555;font-weight:600}
.lead b{color:var(--green);font-weight:600}
.p{font-size:4.6px;line-height:1.55;color:var(--text)}
.h{font-size:6.8px;color:var(--blue)}
.hs{font-size:5.6px;color:var(--blue)}
.ic{width:14px;height:14px;border-radius:50%;background:var(--blue);display:flex;align-items:center;justify-content:center;flex:none}
.ic svg{width:8px;height:8px}
.ic.g{background:var(--green)}
.ic.gr{background:var(--grey)}
.ic.o{background:none;border:1px solid var(--grey)}
.ic.w{background:none;border:1px solid var(--white)}
.row{position:absolute;display:flex;gap:8px;align-items:flex-start}
.photo{position:absolute}
.fill-light{background:linear-gradient(135deg,#e9eef2,#fbfcfd 60%,#dfe6ea)}
.fill-blur{background:linear-gradient(120deg,#f1f2f2,#d9dfe3 55%,#eef0f1)}
.grad{background:linear-gradient(160deg,#2f8a5f 0%,#386a6f 45%,#384275 100%)}
.grad-soft{background:linear-gradient(170deg,#5f9a86 0%,#6f8c98 45%,#4b5585 100%)}
.white{color:var(--white)}
.box{position:absolute;display:flex;align-items:center;gap:6px;padding:0 6px;color:var(--white)}
.box .n{font-size:17px;font-weight:400;border-right:1.5px solid var(--white);padding-right:5px;line-height:20px}
.box .p{color:var(--white)}
.map{position:absolute;left:95px;top:40px;width:272px;height:116px;background:radial-gradient(ellipse at center,#dcdfe3 0%,var(--map) 70%,#f3f4f6 100%);border-radius:4px}
.pin{position:absolute;width:6px;height:6px;border-radius:50%;background:var(--blue)}
</style>
</head>
<body>

<svg width="0" height="0" style="position:absolute">
  <symbol id="i-search" viewBox="0 0 10 10"><circle cx="4.2" cy="4.2" r="2.8" fill="none" stroke="#fff" stroke-width="1.2"/><line x1="6.3" y1="6.3" x2="8.8" y2="8.8" stroke="#fff" stroke-width="1.4"/></symbol>
  <symbol id="i-pen" viewBox="0 0 10 10"><path d="M2 8 L2.4 6.4 L7 1.8 L8.2 3 L3.6 7.6 Z" fill="#fff"/></symbol>
  <symbol id="i-rocket" viewBox="0 0 10 10"><path d="M8.5 1.5 C6 1.5 4 3.2 3.2 5.5 L4.5 6.8 C6.8 6 8.5 4 8.5 1.5Z" fill="#fff"/><path d="M2 8 L3.3 6.7" stroke="#fff" stroke-width="1"/></symbol>
  <symbol id="i-rocket-d" viewBox="0 0 10 10"><path d="M8.5 1.5 C6 1.5 4 3.2 3.2 5.5 L4.5 6.8 C6.8 6 8.5 4 8.5 1.5Z" fill="none" stroke="#777" stroke-width=".8"/><path d="M2 8 L3.3 6.7" stroke="#777" stroke-width=".8"/></symbol>
  <symbol id="i-gear" viewBox="0 0 10 10"><circle cx="5" cy="5" r="2.8" fill="none" stroke="#fff" stroke-width="1.6" stroke-dasharray="1.4 0.8"/><circle cx="5" cy="5" r="1" fill="#fff"/></symbol>
  <symbol id="i-chart" viewBox="0 0 10 10"><rect x="2" y="6" width="1.3" height="2.5" fill="#fff"/><rect x="4.2" y="4.5" width="1.3" height="4" fill="#fff"/><rect x="6.4" y="2.5" width="1.3" height="6" fill="#fff"/></symbol>
  <symbol id="i-people" viewBox="0 0 10 10"><circle cx="3.5" cy="3.8" r="1.3" fill="#fff"/><circle cx="6.5" cy="3.8" r="1.3" fill="#fff"/><path d="M1.3 8 C1.5 6 5.5 6 5.7 8Z M4.3 8 C4.5 6 8.5 6 8.7 8Z" fill="#fff"/></symbol>
  <symbol id="i-trophy" viewBox="0 0 10 10"><path d="M3 1.8 H7 V4 C7 5.5 3 5.5 3 4Z M5 5.5 V7.5 M3.5 8.2 H6.5" fill="none" stroke="#777" stroke-width=".8"/></symbol>
  <symbol id="i-crown" viewBox="0 0 10 10"><path d="M2 7 L2.4 3.5 L4 5 L5 2.8 L6 5 L7.6 3.5 L8 7 Z" fill="none" stroke="#777" stroke-width=".8"/></symbol>
</svg>

<!-- 1 Portfolio Area -->
<section class="slide c1 r1">
  <div class="title">Portfolio <span class="g">Area</span></div>
  <div class="abs hs" style="left:20px;top:45px">Heading Goes Here</div>
  <div class="abs p" style="left:20px;top:54px;width:150px">Lorem ipsum dolor sit amet, consectetur adipiscing elit, sed do eiusmod tempor incididunt ut labore et dolore magna aliqua. Ut enim minim veniam.</div>
  <div class="row" style="left:31px;top:84px"><div class="ic"><svg><use href="#i-search"/></svg></div><div><div class="hs">Your Text Here</div><div class="p">Lorem ipsum dolor sit amet, consectetur<br>adipiscing elit, sed do eiusmod.</div></div></div>
  <div class="row" style="left:31px;top:111px"><div class="ic"><svg><use href="#i-pen"/></svg></div><div><div class="hs">Your Text Here</div><div class="p">Lorem ipsum dolor sit amet, consectetur<br>adipiscing elit, sed do eiusmod.</div></div></div>
  <div class="row" style="left:31px;top:139px"><div class="ic"><svg><use href="#i-rocket"/></svg></div><div><div class="hs">Your Text Here</div><div class="p">Lorem ipsum dolor sit amet, consectetur<br>adipiscing elit, sed do eiusmod.</div></div></div>
  <div class="row" style="left:31px;top:167px"><div class="ic"><svg><use href="#i-gear"/></svg></div><div><div class="hs">Your Text Here</div><div class="p">Lorem ipsum dolor sit amet, consectetur<br>adipiscing elit, sed do eiusmod.</div></div></div>
  <div class="photo fill-light" role="img" aria-label="Window grid photo of a visitor using the sign-in kiosk" style="left:238px;top:0;width:145px;height:198px"></div>
  <div class="footer">© 2016 Verimonta. All rights reserved.<span class="num">16</span><span class="end"></span></div>
</section>

<!-- 2 Two Column Description -->
<section class="slide c2 r1">
  <div class="title">Two Column <span class="g">Description</span></div>
  <div class="logo"><i></i>Verimonta</div>
  <div class="abs lead" style="left:20px;top:68px">We are <b>Verimonta</b></div>
  <div class="abs p" style="left:18px;top:100px;width:168px">Lorem ipsum dolor sit amet, consectetur adipiscing elit, sed do eiusmod tempor incididunt ut labore et dolore magna aliqua. Ut enim ad minim veniam, quis nostrud exercitation ullamco laboris nisi ut aliquip ex ea commodo consequat.<br><br>Duis aute irure dolor in reprehenderit in voluptate velit esse cillum dolore eu fugiat nulla pariatur. Excepteur sint occaecat cupidatat non proident, sunt in culpa qui officia deserunt mollit anim id est laborum.</div>
  <div class="abs" style="left:198px;top:100px;width:1px;height:70px;background:#ddd"></div>
  <div class="abs p" style="left:208px;top:100px;width:160px">Lorem ipsum dolor sit amet, consectetur adipiscing elit, sed do eiusmod tempor incididunt ut labore et dolore magna aliqua. Ut enim ad minim veniam, quis nostrud exercitation ullamco laboris nisi ut aliquip ex ea commodo consequat.<br><br>Duis aute irure dolor in reprehenderit in voluptate velit esse cillum dolore eu fugiat nulla pariatur. Excepteur sint occaecat cupidatat non proident, sunt in culpa qui officia deserunt mollit anim id est laborum.</div>
  <div class="footer">© 2016 Verimonta. All rights reserved.<span class="num">17</span><span class="end"></span></div>
</section>

<!-- 3 Coffee Break -->
<section class="slide c3 r1 grad" role="img" aria-label="Coffee cup on a table, tinted green to blue">
  <div class="logo w lg" style="top:24px"><i></i>Verimonta</div>
  <svg class="abs" style="left:89px;top:70px" width="18" height="20" viewBox="0 0 18 20"><path d="M6 1 C4 3 8 4 6 6 M10 1 C8 3 12 4 10 6" stroke="#fff" fill="none" stroke-width="1.2"/><path d="M2 8 H14 V12 C14 15 11 17 8 17 C5 17 2 15 2 12Z" fill="#fff"/><path d="M14 9 C17 9 17 13 14 13" stroke="#fff" fill="none" stroke-width="1.4"/><rect x="1" y="18" width="14" height="1.5" fill="#fff"/></svg>
  <div class="abs white" style="left:46px;top:95px;font-size:12px;font-weight:600">COFFEE BREAK</div>
  <div class="abs white" style="left:62px;top:112px;font-size:5.5px">Back in 15 minutes</div>
</section>

<!-- 4 Three Column Description -->
<section class="slide c1 r2">
  <div class="title">Three Column <span class="g">Description</span></div>
  <div class="logo"><i></i>Verimonta</div>
  <div class="abs lead" style="left:27px;top:67px">We are <b>Verimonta</b></div>
  <div class="abs p" style="left:20px;top:96px;width:98px">Lorem ipsum dolor sit amet, consectetur adipiscing elit, sed do eiusmod tempor incididunt ut labore et dolore magna aliqua. Ut enim minim veniam, quis nostrud exercitation ullamco laboris nisi ut aliquip ex ea commodo consequat.<br><br>Duis aute irure dolor in reprehenderit in voluptate velit esse cillum dolore eu fugiat nulla pariatur excepteur occaecat.</div>
  <div class="abs p" style="left:143px;top:96px;width:98px">Lorem ipsum dolor sit amet, consectetur adipiscing elit, sed do eiusmod tempor incididunt ut labore et dolore magna aliqua. Ut enim minim veniam, quis nostrud exercitation ullamco laboris nisi ut aliquip ex ea commodo consequat.<br><br>Duis aute irure dolor in reprehenderit in voluptate velit esse cillum dolore eu fugiat nulla pariatur excepteur occaecat.</div>
  <div class="abs" style="left:259px;top:92px;width:1px;height:90px;background:#ddd"></div>
  <div class="abs p" style="left:266px;top:92px;width:98px">Lorem ipsum dolor sit amet, consectetur adipiscing elit, sed do eiusmod tempor incididunt ut labore et dolore magna aliqua. Ut enim minim veniam, quis nostrud exercitation ullamco laboris nisi ut aliquip ex ea commodo consequat.<br><br>Duis aute irure dolor in reprehenderit in voluptate velit esse cillum dolore eu fugiat nulla pariatur excepteur occaecat.</div>
  <div class="footer">© 2016 Verimonta. All rights reserved.<span class="num">19</span><span class="end"></span></div>
</section>

<!-- 5 Feature panel -->
<section class="slide c2 r2">
  <div class="photo fill-blur" role="img" aria-label="Sign-in kiosk tablet on a stand in a bright hallway" style="left:0;top:0;width:383px;height:215px"></div>
  <div class="abs" style="left:228px;top:0;width:136px;height:215px;background:var(--blue)">
    <div class="logo w lg" style="left:28px;right:auto;top:26px"><i></i>Verimonta</div>
    <div class="abs ic w" style="left:14px;top:68px;width:22px;height:22px"><svg><use href="#i-rocket"/></svg></div>
    <div class="abs ic w" style="left:57px;top:68px;width:22px;height:22px"><svg><use href="#i-gear"/></svg></div>
    <div class="abs ic w" style="left:100px;top:68px;width:22px;height:22px"><svg><use href="#i-chart"/></svg></div>
    <div class="abs white" style="left:15px;top:118px;font-size:15px;line-height:1.05">Your Title<br>Goes Here</div>
    <div class="abs p" style="left:15px;top:155px;width:110px;color:#dfe2ee">Lorem ipsum dolor sit amet, consectetur adipiscing elit, sed do eiusmod tempor incididunt ut labore et commodo consequat dolore magna aliqua.</div>
    <div class="abs white" style="left:0;bottom:0;width:136px;height:19px;background:var(--green);font-size:5.5px;text-align:center;line-height:19px">www.yourwebsite.com</div>
  </div>
</section>

<!-- 6 Your Title Goes Here -->
<section class="slide c3 r2">
  <div class="title">Your Title <span class="g">Goes Here</span></div>
  <div class="logo"><i></i>Verimonta</div>
  <div class="abs hs" style="left:17px;top:47px">Heading Goes Here</div>
  <div class="abs p" style="left:17px;top:56px;width:352px">Lorem ipsum dolor sit amet, consectetur adipiscing elit, sed do eiusmod tempor incididunt ut labore et dolore magna aliqua. Ut enim ad minim veniam, quis nostrud exercitation ullamco laboris nisi ut aliquip ex ea commodo consequat.</div>
  <div class="row" style="left:17px;top:79px"><div class="ic"><svg><use href="#i-chart"/></svg></div><div><div class="hs">Service Number One</div><div class="p" style="width:125px">Lorem ipsum dolor sit amet, consectetur adipiscing elit, sed do eiusmod tempor incididunt ut labore et dolore magna aliqua.</div></div></div>
  <div class="row" style="left:17px;top:115px"><div class="ic g"><svg><use href="#i-rocket"/></svg></div><div><div class="hs" style="color:var(--green)">Service Number Two</div><div class="p" style="width:125px">Lorem ipsum dolor sit amet, consectetur adipiscing elit, sed do eiusmod tempor incididunt ut labore et dolore.</div></div></div>
  <div class="row" style="left:17px;top:153px"><div class="ic gr"><svg><use href="#i-search"/></svg></div><div><div class="hs">Service Number One</div><div class="p" style="width:125px">Lorem ipsum dolor sit amet, consectetur adipiscing elit, sed do eiusmod tempor incididunt ut labore et dolore magna aliqua.</div></div></div>
  <div class="box" style="left:200px;top:77px;width:168px;height:30px;background:var(--blue)"><span class="n">1</span><span class="p">Lorem ipsum dolor sit amet, consectetur adipiscing elit, sed do eiusmod tempor incididunt ut labore et dolore magna aliqua.</span></div>
  <div class="box" style="left:200px;top:113px;width:168px;height:30px;background:var(--green)"><span class="n">2</span><span class="p">Lorem ipsum dolor sit amet, consectetur adipiscing elit, sed do eiusmod tempor incididunt ut labore et dolore magna aliqua.</span></div>
  <div class="box" style="left:200px;top:149px;width:168px;height:30px;background:var(--grey)"><span class="n">3</span><span class="p">Lorem ipsum dolor sit amet, consectetur adipiscing elit, sed do eiusmod tempor incididunt ut labore et dolore magna aliqua.</span></div>
  <div class="footer">© 2016 Verimonta. All rights reserved.<span class="num">21</span><span class="end"></span></div>
</section>

<!-- 7 Title with photo grid -->
<section class="slide c1 r3">
  <div class="abs" style="left:17px;top:38px;font-size:15px;line-height:1.05;color:var(--blue)">Your Title<br><span style="border-bottom:1.5px solid var(--green)">Goes Here</span></div>
  <div class="abs p" style="left:17px;top:82px;width:100px">Lorem ipsum dolor sit amet, consectetur adipiscing elit, sed do eiusmod tempor incididunt ut labore et commodo consequat dolore magna aliqua.<br><br>Duis aute irure dolor in reprehenderit in voluptate velit esse cillum dolore eu fugiat nulla pariatur.<br><br>Ut enim ad minim veniam, quis nostrud exercitation ullamco laboris.</div>
  <div class="photo" role="img" aria-label="Doctor with stethoscope" style="left:118px;top:5px;width:131px;height:192px;background:linear-gradient(150deg,#eef1f3,#d6dde2 60%,#f3f5f6)"></div>
  <div class="photo" role="img" aria-label="Hospital corridor" style="left:254px;top:5px;width:122px;height:94px;background:linear-gradient(160deg,#e4ece8,#cfdad6)"></div>
  <div class="photo" role="img" aria-label="Hands using a tablet" style="left:254px;top:103px;width:122px;height:94px;background:linear-gradient(140deg,#f0ece8,#d6d0ca)"></div>
  <div class="footer">© 2016 Verimonta. All rights reserved.<span class="num">22</span><span class="end"></span></div>
</section>

<!-- 8 Your Title -->
<section class="slide c2 r3">
  <div class="title">Your <span class="u">Title</span></div>
  <div class="logo"><i></i>Verimonta</div>
  <div class="abs h" style="left:15px;top:63px">Heading Goes Here</div>
  <div class="abs p" style="left:15px;top:75px;width:100px">Lorem ipsum dolor sit amet, consectetur adipiscing elit, sed do eiusmod tempor incididunt ut labore et commodo consequat dolore magna aliqua.<br><br>Duis aute irure dolor in reprehenderit in voluptate velit esse cillum dolore eu fugiat nulla pariatur.<br><br>Ut enim ad minim veniam, quis nostrud exercitation ullamco laboris nisi ut aliquip ex ea commodo consequat.</div>
  <div class="photo" role="img" aria-label="Nurse signing in at a wall-mounted kiosk" style="left:123px;top:0;width:137px;height:203px;background:linear-gradient(180deg,#6d5e52,#8e8378 45%,#4c4a4a)"></div>
  <div class="row" style="left:272px;top:63px;gap:5px"><div class="ic"><svg><use href="#i-search"/></svg></div><div><div class="hs">Your Text Here</div><div class="p">Lorem ipsum dolor sit amet, adipiscing<br>elit, sed do eiusmod.</div></div></div>
  <div class="row" style="left:272px;top:94px;gap:5px"><div class="ic"><svg><use href="#i-pen"/></svg></div><div><div class="hs">Your Text Here</div><div class="p">Lorem ipsum dolor sit amet, adipiscing<br>elit, sed do eiusmod.</div></div></div>
  <div class="row" style="left:272px;top:125px;gap:5px"><div class="ic"><svg><use href="#i-rocket"/></svg></div><div><div class="hs">Your Text Here</div><div class="p">Lorem ipsum dolor sit amet, adipiscing<br>elit, sed do eiusmod.</div></div></div>
  <div class="row" style="left:272px;top:156px;gap:5px"><div class="ic"><svg><use href="#i-gear"/></svg></div><div><div class="hs">Your Text Here</div><div class="p">Lorem ipsum dolor sit amet, adipiscing<br>elit, sed do eiusmod.</div></div></div>
  <div class="footer">© 2016 Verimonta. All rights reserved.<span class="num">23</span><span class="end"></span></div>
</section>

<!-- 9 Pictures with Bullets -->
<section class="slide c3 r3">
  <div class="title">Pictures with <span class="g">Bullets</span></div>
  <div class="logo"><i></i>Verimonta</div>
  <div class="photo" role="img" aria-label="Row of kiosk product photos" style="left:50px;top:66px;width:283px;height:44px;background:linear-gradient(90deg,#8f8a82,#d8d8d6 30%,#7d7870 50%,#e0e0de 70%,#8a857d)"></div>
  <div class="abs ic" style="left:113px;top:81px"><svg><use href="#i-search"/></svg></div>
  <div class="abs ic" style="left:186px;top:81px"><svg><use href="#i-gear"/></svg></div>
  <div class="abs ic" style="left:258px;top:81px"><svg><use href="#i-people"/></svg></div>
  <div class="abs hs" style="left:50px;top:126px">Heading Goes Here</div>
  <div class="abs p" style="left:50px;top:134px;width:130px">Lorem ipsum dolor sit amet, consectetur adipiscing elit, sed do eiusmod tempor incididunt ut labore et commodo consequat dolore magna aliqua.<br><br>Duis aute irure dolor in reprehenderit in voluptate velit esse cillum dolore eu fugiat nulla pariatur.</div>
  <div class="abs hs" style="left:202px;top:126px">Heading Goes Here</div>
  <div class="abs p" style="left:202px;top:134px;width:130px">Lorem ipsum dolor sit amet, consectetur adipiscing elit, sed do eiusmod tempor incididunt ut labore et commodo consequat dolore magna aliqua.<br><br>Duis aute irure dolor in reprehenderit in voluptate velit esse cillum dolore eu fugiat nulla pariatur.</div>
  <div class="footer">© 2016 Verimonta. All rights reserved.<span class="num">24</span><span class="end"></span></div>
</section>

<!-- 10 Divider -->
<section class="slide c1 r4 grad-soft" role="img" aria-label="Kiosk on a wooden table, tinted green to blue">
  <div class="logo w lg" style="left:38px;right:auto;top:26px"><i></i>Verimonta</div>
  <div class="abs white" style="right:16px;top:132px;font-size:5.5px">Divider Page</div>
  <div class="abs white" style="right:16px;top:142px;font-size:14px">Your Title Goes Here</div>
  <div class="abs white" style="right:16px;top:162px;font-size:7px">Your Subtitle Here</div>
</section>

<!-- 11 Paragraph with Three Bullet -->
<section class="slide c2 r4">
  <div class="title">Paragraph <span class="u">with</span> <span class="g">Three Bullet</span></div>
  <div class="logo"><i></i>Verimonta</div>
  <div class="abs lead" style="left:20px;top:69px">We are <b>Verimonta</b></div>
  <div class="abs p" style="left:20px;top:97px;width:100px">Lorem ipsum dolor sit amet, consectetur adipiscing elit, sed do eiusmod tempor incididunt ut labore et dolore magna aliqua. Ut enim minim veniam, quis nostrud exercitation ullamco laboris nisi ut aliquip ex ea commodo consequat.<br><br>Duis aute irure dolor in reprehenderit in voluptate velit esse cillum dolore eu fugiat nulla pariatur excepteur occaecat.</div>
  <div class="abs" style="left:135px;top:94px;width:1px;height:90px;background:#ddd"></div>
  <div class="abs" style="left:145px;top:86px;width:225px;display:flex;justify-content:space-between;text-align:center">
    <div style="width:68px"><div class="ic o" style="margin:0 auto 5px;width:18px;height:18px"><svg><use href="#i-trophy"/></svg></div><div class="hs" style="font-size:5px">Your Text Here</div><div class="p">Lorem ipsum dolor sit amet, consectetur adipiscing elit, sed do eiusmod incididunt ut labore et aliqua.<br><br>Ut enim ad minim veniam, quis nostrud exercitation ullamco laboris nisi ut commodo consequat.</div></div>
    <div style="width:68px"><div class="ic o" style="margin:0 auto 5px;width:18px;height:18px"><svg><use href="#i-crown"/></svg></div><div class="hs" style="font-size:5px">Your Text Here</div><div class="p">Lorem ipsum dolor sit amet, consectetur adipiscing elit, sed do eiusmod incididunt ut labore et aliqua.<br><br>Ut enim ad minim veniam, quis nostrud exercitation ullamco laboris nisi ut commodo consequat.</div></div>
    <div style="width:68px"><div class="ic o" style="margin:0 auto 5px;width:18px;height:18px"><svg><use href="#i-rocket-d"/></svg></div><div class="hs" style="font-size:5px">Your Text Here</div><div class="p">Lorem ipsum dolor sit amet, consectetur adipiscing elit, sed do eiusmod incididunt ut labore et aliqua.<br><br>Ut enim ad minim veniam, quis nostrud exercitation ullamco laboris nisi ut commodo consequat.</div></div>
  </div>
  <div class="footer">© 2016 Verimonta. All rights reserved.<span class="num">26</span><span class="end"></span></div>
</section>

<!-- 12 Global Experience -->
<section class="slide c3 r4">
  <div class="title"><span class="u">Global</span> <span class="g">Experience</span></div>
  <div class="logo"><i></i>Verimonta</div>
  <div class="map" role="img" aria-label="Grey world map with office locations marked in blue"></div>
  <div class="abs" style="left:17px;top:163px;width:10px;height:10px;border-radius:50%;background:var(--blue)"></div>
  <div class="abs hs" style="left:32px;top:164px">Heading Goes Here</div>
  <div class="abs p" style="left:17px;top:176px;width:230px">Lorem ipsum dolor sit amet, consectetur adipiscing elit, sed do eiusmod tempor incididunt ut labore et dolore magna aliqua.</div>
  <div class="footer">© 2016 Verimonta. All rights reserved.<span class="num">27</span><span class="end"></span></div>
</section>

<!-- 13 Multiple Column Area -->
<section class="slide c1 r5">
  <div class="title">Multiple <span class="u">Column</span> <span class="g">Area</span></div>
  <div class="logo"><i></i>Verimonta</div>
  <div class="abs" style="left:22px;top:60px;width:340px;display:flex;justify-content:space-between;text-align:center">
    <div style="width:60px"><div class="ic" style="margin:0 auto 3px"><svg><use href="#i-gear"/></svg></div><div class="hs" style="font-size:5px">Your Text Here</div><div class="p">Lorem ipsum<br>consectetur adipiscing<br>elit.</div></div>
    <div style="width:60px"><div class="ic" style="margin:0 auto 3px"><svg><use href="#i-rocket"/></svg></div><div class="hs" style="font-size:5px">Your Text Here</div><div class="p">Lorem ipsum<br>consectetur adipiscing<br>elit.</div></div>
    <div style="width:60px"><div class="ic" style="margin:0 auto 3px"><svg><use href="#i-search"/></svg></div><div class="hs" style="font-size:5px">Your Text Here</div><div class="p">Lorem ipsum<br>consectetur adipiscing<br>elit.</div></div>
    <div style="width:60px"><div class="ic" style="margin:0 auto 3px"><svg><use href="#i-pen"/></svg></div><div class="hs" style="font-size:5px">Your Text Here</div><div class="p">Lorem ipsum<br>consectetur adipiscing<br>elit.</div></div>
    <div style="width:60px"><div class="ic" style="margin:0 auto 3px"><svg><use href="#i-chart"/></svg></div><div class="hs" style="font-size:5px">Your Text Here</div><div class="p">Lorem ipsum<br>consectetur adipiscing<br>elit.</div></div>
  </div>
  <div class="abs" style="left:26px;top:115px;width:332px;height:1px;background:#ddd"></div>
  <div class="abs h" style="left:27px;top:129px">Heading Goes Here</div>
  <div class="abs p" style="left:27px;top:140px;width:155px">Lorem ipsum dolor sit amet, consectetur adipiscing elit, sed do eiusmod tempor incididunt ut labore et commodo consequat dolore magna aliqua.<br><br>Duis aute irure dolor in reprehenderit in voluptate velit esse cillum dolore eu fugiat nulla pariatur.</div>
  <div class="abs h" style="left:207px;top:129px">Heading Goes Here</div>
  <div class="abs p" style="left:207px;top:140px;width:155px">Lorem ipsum dolor sit amet, consectetur adipiscing elit, sed do eiusmod tempor incididunt ut labore et commodo consequat dolore magna aliqua.<br><br>Duis aute irure dolor in reprehenderit in voluptate velit esse cillum dolore eu fugiat nulla pariatur.</div>
  <div class="footer">© 2016 Verimonta. All rights reserved.<span class="num">28</span><span class="end"></span></div>
</section>

<!-- 14 Feature band -->
<section class="slide c2 r5">
  <div class="abs grad-soft" role="img" aria-label="Kiosk on a table, tinted green to blue" style="left:0;top:0;width:383px;height:122px"></div>
  <div class="logo w lg" style="left:32px;right:auto;top:36px"><i></i>Verimonta</div>
  <div class="abs white" style="left:195px;top:47px;font-size:15px">Your Title Goes Here</div>
  <div class="abs p" style="left:195px;top:71px;width:172px;color:#eef0f5">Lorem ipsum dolor sit amet, consectetur adipiscing elit, sed do eiusmod tempor incididunt ut labore et commodo consequat dolore magna aliqua. Duis aute irure dolor in reprehenderit in voluptate velit esse cillum dolore.</div>
  <div class="photo" role="img" aria-label="Sign-in kiosk on a wooden desk" style="left:32px;top:66px;width:131px;height:106px;background:linear-gradient(180deg,#f4f4f4 0%,#e8e8e8 70%,#8a7a68 72%,#6e5f50 100%)"></div>
  <div class="row" style="left:175px;top:133px;gap:5px"><div class="ic"><svg><use href="#i-search"/></svg></div><div><div class="hs">Your Text Here</div><div class="p">Lorem ipsum dolor sit amet,<br>consectetur adipiscing elit, sed<br>do eiusmod.</div></div></div>
  <div class="row" style="left:273px;top:133px;gap:5px"><div class="ic"><svg><use href="#i-pen"/></svg></div><div><div class="hs">Your Text Here</div><div class="p">Lorem ipsum dolor sit amet,<br>consectetur adipiscing elit, sed<br>do eiusmod.</div></div></div>
  <div class="row" style="left:175px;top:166px;gap:5px"><div class="ic"><svg><use href="#i-gear"/></svg></div><div><div class="hs">Your Text Here</div><div class="p">Lorem ipsum dolor sit amet,<br>consectetur adipiscing elit, sed<br>do eiusmod.</div></div></div>
  <div class="row" style="left:273px;top:166px;gap:5px"><div class="ic"><svg><use href="#i-rocket"/></svg></div><div><div class="hs">Your Text Here</div><div class="p">Lorem ipsum dolor sit amet,<br>consectetur adipiscing elit, sed<br>do eiusmod.</div></div></div>
  <div class="footer">© 2016 Verimonta. All rights reserved.<span class="num">29</span><span class="end"></span></div>
</section>

<!-- 15 Divider with band -->
<section class="slide c3 r5 grad-soft" role="img" aria-label="Kiosk on a wooden table, tinted green to blue">
  <div class="logo w lg" style="top:26px"><i></i>Verimonta</div>
  <div class="abs" style="left:145px;top:118px;width:238px;height:44px;background:var(--blue)"></div>
  <div class="abs" style="left:145px;top:118px;width:44px;height:44px;background:var(--green)"></div>
  <div class="abs white" style="left:198px;top:120px;font-size:5.5px">Divider Page</div>
  <div class="abs white" style="left:198px;top:128px;font-size:14px">Your Title Goes Here</div>
  <div class="abs white" style="left:198px;top:148px;font-size:7px">Your Subtitle Here</div>
</section>

</body>
</html>
```